Business Card Design Project

We need a Business Card for an Mechanical Engineering firm in Singapore. The design should be Modern & Technical looking, yet eye catching.

Our company deals in Cutting Tools & Machine Accessories for the Manufacturing Industries such as Oil & Gas, Aero Space, etc... For more information on our Company, you can either email me or view our website www.valtrion.com.sg.

We are trying to revamp our image to give our consumers a fresh new perspective to our company, so we welcome all ideas.

Industry/Entity Type

Business

Requirements
Must have
• Must incorporate New Company Logo into the card as shown in Uploaded file.

```html
<!DOCTYPE html>
<html lang="en">
<head>
<meta charset="utf-8">
<title>Valtrion Tools – Business Card</title>
<link rel="stylesheet" href="https://fonts.googleapis.com/css2?family=Saira+Condensed:wght@400;500&display=swap">
<style>
  :root {
    --page: #ffffff;
    --card-dark: #070809;
    --card-light: #ffffff;
    --accent: #9c1a30;
    --accent-deep: #5e0f1d;
    --ink: #151515;
    --white: #ffffff;
    --edge: rgba(0, 0, 0, 0.18);
  }
  * { margin: 0; padding: 0; box-sizing: border-box; }
  html, body {
    width: 871px;
    height: 1200px;
    overflow: hidden;
    background: var(--page);
  }
  .canvas {
    position: relative;
    width: 871px;
    height: 1200px;
    font-family: "Saira Condensed", "Arial Narrow", sans-serif;
  }
  .card {
    position: absolute;
    left: 118px;
    width: 635px;
    overflow: hidden;
  }
  .card--front {
    top: 113px;
    height: 410px;
    background: var(--card-dark);
  }
  .card--back {
    top: 680px;
    height: 400px;
    background: var(--card-light);
    box-shadow: 0 0 0 1px var(--edge);
  }
  .front-artwork {
    position: absolute;
    left: 0;
    top: 0;
    width: 360px;
    height: 410px;
  }
  .contact {
    position: absolute;
    left: 357px;
    top: 180px;
  }
  .contact__name {
    color: var(--white);
    font-size: 28px;
    font-weight: 400;
    line-height: 1;
    letter-spacing: 0.5px;
    margin-bottom: 22px;
  }
  .contact__phone {
    color: var(--accent);
    font-size: 29px;
    line-height: 1;
    letter-spacing: 1px;
    margin-bottom: 8px;
  }
  .contact__line {
    color: var(--accent);
    font-size: 22px;
    line-height: 32px;
  }
  .brand {
    position: absolute;
    left: 0;
    right: 0;
    top: 210px;
    display: flex;
    justify-content: center;
    align-items: center;
    gap: 16px;
  }
  .brand__mark {
    width: 30px;
    height: 30px;
    background: var(--accent);
  }
  .brand__name {
    color: var(--ink);
    font-size: 58px;
    font-weight: 400;
    line-height: 1;
    letter-spacing: 1px;
  }
</style>
</head>
<body>
<main class="canvas">
  <section class="card card--front">
    <svg class="front-artwork" viewBox="0 0 360 410" role="img" aria-label="Interlocking red machine gears with fine flowing wave lines">
      <defs>
        <linearGradient id="gear-glow" x1="0" y1="0" x2="1" y2="0.3">
          <stop offset="0" stop-color="#9c1a30"/>
          <stop offset="0.45" stop-color="#5e0f1d"/>
          <stop offset="1" stop-color="#070809" stop-opacity="0"/>
        </linearGradient>
      </defs>
      <path d="M0 0 H250 C200 80 200 140 260 220 C320 300 350 360 352 410 H0 Z" fill="url(#gear-glow)"/>
    </svg>
    <div class="contact">
      <p class="contact__name">YOUR NAME HEAR</p>
      <p class="contact__phone">0000 999 999 999</p>
      <p class="contact__line">Address here Address here</p>
      <p class="contact__line">www.valtrion.com.sg</p>
      <p class="contact__line">Email here Email here</p>
    </div>
  </section>

  <section class="card card--back">
    <div class="brand">
      <span class="brand__mark" aria-hidden="true"></span>
      <span class="brand__name">VALTRION TOOLS</span>
    </div>
  </section>
</main>
</body>
</html>
```